Stationary Set Rebrand for Brenton

We are a Canadian Distribution and Service Company that was established in 1969. Over the past 5 decades we have expanded our business and have warehouses across Canada. We specialize in adhesive tapes, adhesives, films, safety, warehouse, shipping, janitorial and packaging supplies.

We have updated our logo design and would like a new corporate branding identity that includes a new fresh Stationary Set (Business Cards, Letterhead, Letterhead MS Word, Envelope, Presentation Folders, Email Signatures, Notepad Covers, etc.)

Target Market(s)

Industrial Business Sector

Font styles to use
Sans Serif

Colors
0054AA
0677BA
7BADD7
CADEEF
E8F1F8
0094D4
00A9DD
6FCCEA
C7EBF8
E9F6FB
00AB8E
00BBA5
67D7C9
C6EFE9
E9F9F6
EB3D1F
EC4F4E
F09395
F8D3D4
FCEDEE

Requirements
Should not have
• Colors not too light, darker colours preferred

```html
<!DOCTYPE html>
<html lang="en">
<head>
<meta charset="utf-8">
<title>Brenton Stationery Set</title>
<link rel="stylesheet" href="https://fonts.googleapis.com/css2?family=Montserrat:wght@400;500;600;800&family=Great+Vibes&display=swap">
<style>
:root{
  --bg:#b6b5b6;
  --paper:#ffffff;
  --ink:#1b1b1b;
  --dark:#161616;
  --red:#d71f27;
  --grey:#6b6b6b;
  --rule:#9a9a9a;
  --stripe:#ececec;
  --shadow:0 2px 4px rgba(0,0,0,.35);
}
*{box-sizing:border-box;margin:0;padding:0}
html,body{width:874px;height:1200px;overflow:hidden}
body{background:var(--bg);font-family:"Montserrat",Arial,sans-serif;color:var(--ink);position:relative}
.item{position:absolute;background:var(--paper);box-shadow:var(--shadow);overflow:hidden}
.dark{background:var(--dark);color:#fff}
.pattern{background:linear-gradient(135deg,#3a3a3a 0%,#151515 45%,#2c2c2c 70%,#111 100%)}

/* brand lockup */
.brand{display:inline-block;line-height:1}
.brand-row{display:flex;align-items:center;gap:.15em}
.brand-name{font-weight:800;letter-spacing:-.02em}
.brand-mark{width:.32em;height:.32em;background:var(--red);display:inline-block}
.brand-tag{font-weight:500;font-size:.2em;letter-spacing:.01em;margin-top:.25em}

.contact{font-size:5px;line-height:1.5;color:var(--ink)}
.contact .ico{color:var(--red);margin-right:2px}
.vrule{position:absolute;width:1px;background:var(--red)}

/* business cards */
.card-back{left:87px;top:47px;width:140px;height:80px;border-radius:5px}
.card-front{left:87px;top:138px;width:140px;height:79px;border-radius:5px}
.card-front .brand{position:absolute;left:15px;top:8px;font-size:28px;color:#fff}
.card-front .person{position:absolute;right:76px;top:44px;text-align:right}
.card-front .person b{display:block;color:var(--red);font-size:6.3px;font-weight:600}
.card-front .person span{font-size:4px}
.card-front .vrule{left:69px;top:44px;height:18px}
.card-front .contact{position:absolute;left:74px;top:43px;color:#fff;font-size:3.6px}
.card-front .band{position:absolute;left:0;right:0;bottom:6px;height:5px;background:var(--red);font-size:3.3px;color:#fff;padding-left:38px;line-height:5px}
.card-front .qr{position:absolute;right:18px;bottom:4px;width:13px;height:13px;background:#fff;border:2px solid #333}

/* envelopes */
.env-front{left:279px;top:50px;width:176px;height:77px}
.env-front .brand{position:absolute;left:9px;top:6px;font-size:12px}
.env-front .addr{position:absolute;left:63px;top:8px;font-size:2.8px;line-height:1.4;border-left:1px solid var(--red);padding-left:3px}
.env-back{left:278px;top:140px;width:177px;height:77px}
.env-back .flap{position:absolute;left:0;top:0;width:177px;height:28px}

/* presentation folder */
.folder-cover{left:545px;top:58px;width:224px;height:138px;display:flex}
.folder-cover .panel{position:relative;width:50%;height:100%}
.folder-cover .brand{position:absolute;left:10px;top:42px;font-size:22px}
.folder-cover .foot{position:absolute;left:10px;right:10px;bottom:14px;border-top:1px solid var(--red);font-size:2.8px;padding-top:2px}
.folder-open{left:540px;top:210px;width:245px;height:135px;display:flex;background:#e4e4e4}
.folder-open .side{position:relative;width:50%;height:100%;overflow:hidden}
.folder-open .pocket{position:absolute;left:0;right:0;bottom:0;height:46px}
.folder-open .insert{position:absolute;left:14px;top:10px;width:92px;height:100px;background:#fff;box-shadow:0 1px 2px rgba(0,0,0,.3)}
.folder-open .insert .brand{position:absolute;left:6px;top:6px;font-size:8px}
.folder-open .insert .lines{position:absolute;left:6px;right:6px;top:34px}
.folder-open .insert .lines i{display:block;height:1px;background:#c8c8c8;margin-bottom:3px}

/* notebooks */
.note-cover{left:64px;top:276px;width:116px;height:164px;border-radius:2px}
.spiral{position:absolute;top:0;bottom:0;width:8px;background:repeating-linear-gradient(to bottom,transparent 0 3px,#222 3px 5px,transparent 5px 9px)}
.note-cover .spiral{left:-2px}
.note-open{left:248px;top:277px;width:232px;height:163px;display:flex;background:none;box-shadow:none;overflow:visible}
.page{position:relative;width:50%;height:100%;background:#fbfbfb;box-shadow:var(--shadow);padding:8px 6px}
.page .brand{font-size:11px}
.page .date{position:absolute;right:6px;top:12px;font-size:3.4px;color:var(--grey)}
.page .ruled{position:absolute;left:6px;right:6px;top:28px;bottom:10px;background:repeating-linear-gradient(to bottom,transparent 0 7px,#7d7d7d 7px 7.6px)}
.note-open .spiral{left:112px;height:163px;z-index:2}

/* logo card */
.logo-card{left:560px;top:402px;width:265px;height:124px;display:flex;align-items:center;justify-content:center}
.logo-card .brand{font-size:52px}

/* email signature */
.signature{left:56px;top:491px;width:430px;height:137px}
.signature .brand{position:absolute;left:60px;top:40px;font-size:42px}
.signature .vrule{left:238px;top:18px;height:102px;width:1.2px}
.signature .who{position:absolute;left:256px;top:16px}
.signature .who b{display:block;font-size:15px;color:var(--red);font-weight:600}
.signature .who span{font-size:9px;color:#444}
.signature .contact{position:absolute;left:256px;top:52px;font-size:9px;line-height:1.45;color:#444}
.signature .contact p.gap{margin-top:4px}

/* compliments slip */
.slip{left:558px;top:557px;width:264px;height:125px}
.slip .brand{position:absolute;left:10px;top:12px;font-size:28px}
.slip .contact{position:absolute;left:188px;top:11px;font-size:5px}
.slip .script{position:absolute;right:12px;bottom:16px;font-family:"Great Vibes",cursive;font-size:20px}

/* invoice */
.invoice{left:135px;top:735px;width:282px;height:399px}
.invoice .brand,.letter .brand{position:absolute;left:17px;top:22px;font-size:31px}
.doc-head .vrule{left:193px;top:20px;height:38px}
.doc-head .contact{position:absolute;left:200px;top:20px}
.invoice .title{position:absolute;left:17px;top:88px;font-size:7.5px;font-weight:600;color:var(--red)}
.invoice .date{position:absolute;left:208px;top:91px;font-size:5px}
.field{position:absolute;left:17px;font-size:5px;display:flex;gap:2px;align-items:flex-end}
.field i{display:block;border-bottom:.6px solid #555;height:5px}
.inv-table{position:absolute;left:17px;top:141px;width:248px;border-collapse:collapse;font-size:5.5px}
.inv-table th{background:var(--red);color:#fff;font-weight:500;height:14px;border:.6px solid var(--red)}
.inv-table td{height:14.4px;border-left:.6px solid var(--red);border-right:.6px solid var(--red)}
.inv-table tr:nth-child(even) td{background:var(--stripe)}
.inv-table tr:last-child td{border-bottom:.6px solid var(--red)}
.pay{position:absolute;left:17px;top:330px;display:flex;gap:8px;font-size:4.2px;color:#555}
.pay span::before{content:"";display:inline-block;width:5px;height:5px;border:.6px solid var(--red);margin-right:3px;vertical-align:-1px}
.totals{position:absolute;left:178px;top:317px;width:87px;border-collapse:collapse;font-size:5.3px}
.totals td{border:.6px solid var(--red);height:14.5px;padding-left:4px}
.totals td+td{width:43px}
.accept{position:absolute;left:17px;top:347px;font-size:5px;line-height:1.4}

/* letterhead */
.letter{left:454px;top:735px;width:281px;height:398px}
.letter .brand{left:26px;top:17px}
.letter .doc-head .vrule{left:182px;top:15px}
.letter .doc-head .contact{left:189px;top:15px}
.letter .recipient{position:absolute;left:26px;top:94px;font-size:5px;line-height:1.5}
.letter .recipient b{font-weight:500;font-size:5.3px}
.letter .recipient span{font-size:3.8px;display:block}
.letter .body{position:absolute;left:26px;right:26px;top:142px;font-size:3.6px;line-height:1.75;text-align:justify;color:#444}
.letter .body p{margin-bottom:6px}
.letter .closing{position:absolute;left:26px;top:296px;font-size:4.2px}
.letter .sign{display:block;width:36px;height:10px;margin:4px 0;background:linear-gradient(90deg,#333,#777);border-radius:4px}
.letter .closing b{font-weight:400;font-size:5.3px}
</style>
</head>
<body>

<!-- business card back -->
<div class="item dark card-back pattern" role="img" aria-label="Dark tonal leaf pattern with one red accent"></div>

<!-- business card front -->
<div class="item dark card-front">
  <div class="brand"><div class="brand-row"><span class="brand-name">Brenton</span></div><div class="brand-tag">Tape and Packaging Specialists</div></div>
  <div class="person"><b>Daniel Harcourt</b><span>Managing Director</span></div>
  <div class="vrule"></div>
  <div class="contact"><p><span class="ico">☎</span>123 456 789</p><p><span class="ico">✉</span>info@brentonmail.com</p><p><span class="ico">●</span>www.brentonsupply.com</p></div>
  <div class="band">Your address, City State, Zip 1234</div>
  <div class="qr" role="img" aria-label="QR code"></div>
</div>

<!-- envelope front -->
<div class="item env-front">
  <div class="brand"><div class="brand-row"><span class="brand-name">Brenton</span></div><div class="brand-tag">Tape and Packaging Specialists</div></div>
  <div class="addr">Your address, City<br>State, Zip 1234</div>
</div>

<!-- envelope back -->
<div class="item env-back">
  <svg class="flap" viewBox="0 0 177 28" aria-hidden="true"><path d="M0 0H177L170 22Q168 28 160 28H17Q9 28 7 22Z" fill="#161616"/></svg>
</div>

<!-- folder cover -->
<div class="item folder-cover">
  <div class="panel">
    <div class="brand"><div class="brand-row"><span class="brand-name">Brenton</span></div><div class="brand-tag">Tape and Packaging Specialists</div></div>
    <div class="foot">☎ 123 456 789 · info@brentonmail.com · www.brentonsupply.com</div>
  </div>
  <div class="panel pattern" role="img" aria-label="Dark tonal leaf pattern with one red accent"></div>
</div>

<!-- folder open -->
<div class="item folder-open">
  <div class="side"><div class="pocket" style="background:var(--dark)"></div></div>
  <div class="side" style="background:#f1f1f1">
    <div class="insert">
      <div class="brand"><div class="brand-row"><span class="brand-name">Brenton</span></div></div>
      <div class="lines"><i></i><i></i><i></i><i></i><i></i><i></i><i></i><i></i><i></i><i></i></div>
    </div>
    <div class="pocket" style="background:var(--red)"></div>
  </div>
</div>

<!-- notebook cover -->
<div class="item note-cover pattern" role="img" aria-label="Dark tonal leaf pattern with one red accent"><div class="spiral"></div></div>

<!-- notebook open -->
<div class="item note-open">
  <div class="page">
    <div class="brand"><div class="brand-row"><span class="brand-name">Brenton</span></div><div class="brand-tag">Tape and Packaging Specialists</div></div>
    <div class="date">Date……/……/……</div><div class="ruled"></div>
  </div>
  <div class="spiral"></div>
  <div class="page">
    <div class="brand"><div class="brand-row"><span class="brand-name">Brenton</span></div><div class="brand-tag">Tape and Packaging Specialists</div></div>
    <div class="date">Date……/……/……</div><div class="ruled"></div>
  </div>
</div>

<!-- logo card -->
<div class="item logo-card">
  <div class="brand"><div class="brand-row"><span class="brand-name">Brenton</span><span class="brand-mark"></span></div><div class="brand-tag">Tape and Packaging Specialists</div></div>
</div>

<!-- email signature -->
<div class="item signature">
  <div class="brand"><div class="brand-row"><span class="brand-name">Brenton</span></div><div class="brand-tag">Tape and Packaging Specialists</div></div>
  <div class="vrule"></div>
  <div class="who"><b>Daniel Harcourt</b><span>Managing Director</span></div>
  <div class="contact">
    <p>Your address, City</p><p>State, Zip 1234</p>
    <p class="gap"><span class="ico">☎</span>123 456 789</p>
    <p><span class="ico">✉</span>info@brentonmail.com</p>
    <p><span class="ico">●</span>www.brentonsupply.com</p>
  </div>
</div>

<!-- compliments slip -->
<div class="item slip">
  <div class="brand"><div class="brand-row"><span class="brand-name">Brenton</span></div><div class="brand-tag">Tape and Packaging Specialists</div></div>
  <div class="contact"><p>Your address, City</p><p>State, Zip 1234</p><p style="margin-top:3px"><span class="ico">☎</span>123 456 789</p><p><span class="ico">✉</span>info@brentonmail.com</p><p><span class="ico">●</span>www.brentonsupply.com</p></div>
  <div class="script">with compliments</div>
</div>

<!-- invoice -->
<div class="item invoice">
  <div class="brand"><div class="brand-row"><span class="brand-name">Brenton</span></div><div class="brand-tag">Tape and Packaging Specialists</div></div>
  <div class="doc-head"><div class="vrule"></div>
    <div class="contact"><p>Your address, City</p><p>State, Zip 1234</p><p style="margin-top:3px"><span class="ico">☎</span>123 456 789</p><p><span class="ico">✉</span>info@brentonmail.com</p><p><span class="ico">●</span>www.brentonsupply.com</p></div>
  </div>
  <div class="title">INVOICE# :</div>
  <div class="date">DATE:</div>
  <div class="field" style="top:104px">Customer :<i style="width:220px"></i></div>
  <div class="field" style="top:115px">Address :<i style="width:223px"></i></div>
  <div class="field" style="top:126px">Phone :<i style="width:111px"></i>&nbsp;Fax :<i style="width:99px"></i></div>
  <table class="inv-table">
    <tr><th style="width:32px">QTY</th><th style="width:128px">DESCRIPTION</th><th style="width:44px">PRICE</th><th>AMOUNT</th></tr>
    <tr><td></td><td></td><td></td><td></td></tr><tr><td></td><td></td><td></td><td></td></tr>
    <tr><td></td><td></td><td></td><td></td></tr><tr><td></td><td></td><td></td><td></td></tr>
    <tr><td></td><td></td><td></td><td></td></tr><tr><td></td><td></td><td></td><td></td></tr>
    <tr><td></td><td></td><td></td><td></td></tr><tr><td></td><td></td><td></td><td></td></tr>
    <tr><td></td><td></td><td></td><td></td></tr><tr><td></td><td></td><td></td><td></td></tr>
    <tr><td></td><td></td><td></td><td></td></tr>
  </table>
  <div class="pay"><span>VISTA</span><span>MC</span><span>DEBIT</span><span>CASH</span><span>CHEQUE</span></div>
  <table class="totals"><tr><td>SUB TOTAL</td><td></td></tr><tr><td>GUST</td><td></td></tr><tr><td>SUBBTOTAL</td><td></td></tr></table>
  <div class="accept">Signature Indicates<br>Acceptance of Price and term</div>
</div>

<!-- letterhead -->
<div class="item letter">
  <div class="brand"><div class="brand-row"><span class="brand-name">Brenton</span></div><div class="brand-tag">Tape and Packaging Specialists</div></div>
  <div class="doc-head"><div class="vrule"></div>
    <div class="contact"><p>Your address, City</p><p>State, Zip 1234</p><p style="margin-top:3px"><span class="ico">☎</span>123 456 789</p><p><span class="ico">✉</span>info@brentonmail.com</p><p><span class="ico">●</span>www.brentonsupply.com</p></div>
  </div>
  <div class="recipient"><b>SOFIA MARCHETTI</b><span>Chief Exective Officer</span><span>City/State, Zip Code</span></div>
  <div class="body">
    <p>Proin gravida nibh vel velit auctor aliquet. Aenean sollicitudin, lorem quis bibendum auctor, nisi elit consequat ipsum, nec sagittis sem nibh id elit. Duis sed odio sit amet nibh vulputate cursus a sit amet mauris. Morbi accumsan ipsum velit. Nam nec tellus a odio tincidunt auctor a ornare odio. Sed non mauris vitae erat consequat auctor eu in elit. Class aptent taciti sociosqu ad litora torquent ugue. Sed non neque elit. Sed ut imperdiet nisi. Proin condimentum fermentum nunc. Etiam pharetra, imperdiet nisi. Proin condimentum fermentum nunc. Etiam pharetra, erat sed fermentum feugiat, velit mauris egestas quam, ut aliquam massa nisl quis neque. Suspendisse in orci enim.</p>
    <p>This is Photoshop's version of Lorem Ipsum. Proin gravida nibh vel velit auctor aliquet. Aenean sollicitudin, lorem quis bibendum auctor, nisi elit consequat ipsum, nec sagittis sem nibh id elit. Duis sed odio sit amet nibh vulputate cursus a sit amet mauris. Morbi accumsan ipsum velit. Nam nec tellus a odio tincidunt auctor a ornare odio. Sed non mauris vitae erat consequat auctor eu in elit. Class aptent taciti sociosqu ad litora torquent per conubia nostra, per inceptos himenaeos. Mauris in erat justo.</p>
    <p>Nullam ac urna eu felis dapibus condimentum sit amet a augue. Sed non neque elit. Sed ut imperdiet nisi. Proin condimentum fermentum nunc. Etiam pharetra, erat sed fermentum feugiat, velit mauris egestas quam. Nullam ac urna eu felis dapibus condimentum sit amet a augue pharetra, erat sed fermentum feugiat, velit mauris egestas quam. Sed non neque elit. Sed ut imperdiet nisi. Proin condimentum fermentum nunc.</p>
  </div>
  <div class="closing">Sincerely,<span class="sign" role="img" aria-label="Handwritten signature"></span><b>Owen Pritchard</b></div>
</div>

</body>
</html>
```